Brennick Setter Club - Rare dog breed club needs web design!

The Transylvanian Hound (or Erdélyi kopó) is an ancient Hungarian dog breed. These medium-sized hounds were favored by the Hungarian kings and princes for hunting bears and wolves in the Carpathian mountains of Transylvania. The breed's great adaptability to the region's extreme climates of sweltering summers and frigid winters made it an excellent all season hunting dog. This dog has a sleek appearance and stunning good looks. They are lean, appear very elegant and proud. Their erect posture and beautifully sculpted head portray great attentiveness and authority. In general, this rare breed is extremely good natured, loyal and obedient. It has a tendency to form strong attachments to its primary caretakers and will remain loyal and protective. (Please refer to existing web resources.)

The Brennick Setter Club - with current website www.brennicksetter.com - is the official breed club of Transylvanian Hound afficionados, breeders and owners in the United States, which was founded in 2010. We are looking for a web design for the new, upgraded version of this central (currenty non-functioning) website. Please do not recycle the old logo (we may choose from your suggesions and pay for it!) or any of the old texts. Please use the structure described below. Overall, the webpage serves a dual purpose: an educational one (about the breed itself) and a community-building one (inside the Club). The proposed structure of the website is as follows:

1. About the Kopó
- Breed History
- Breed Standard
- Public Education
- Photo Gallery

2. Life with a Kopó
- Health and Genetics
- Feeding and Nutrition
- Training and Activities

3. Finding a Kopó
- Is this the Right Breed for You?
- Choosing a Puppy
- FAQ
- Breeder Referral

4. The Brennick Setter Club
- Constituton
- Officers and Appointees
- Code of Ethics
- Breeder Guidelines
- Membership
- Reports
- Links

5. News and Events

6. Shop

We are attaching a couple of examples of the graphics/drawings of the dogs that would be part of the design of the website. We plan to have more of these artistic depictions, nicely embedded into the background (maybe shaded out at the edges just like the drawings themselves) and less actual photos. Or a good combination of the two.

Further information upon request.

Reason: There are a few very promising design collaborations ongoing. As we moved the brief to a more artistic and graphic direction, we felt that one week of extension would be needed to get to the perfect end-product, which could include designs for sub-pages as well.

Reason: In order to make the final modifications to the leading designs, and at the request of those designers, the deadline is extended until Friday.

Target Market(s)

- BRSC Club members, dog (especially T-Hound) owners, past and future owners, breeders, puppy buyers, hunters, kennel clubs, dog show participants, vets, animal shelters, Hungarian, Romanian and other European web visitors, historians

Industry/Entity Type

Club

Font styles to use
Serif
Decorative
Script

Requirements
Must have
• - Sync with graphics of dogs (see attachments), but accentuate the rich black basic color of the dogs
- Elegance, aristocratic/noble look and feel (but not overly archaic)
- Love, companionship, dogs as family members
- Hunting usage, but no bloody associations, rather romantic ones
- Simple to use and navigate for non-web-natives
- Old world (Central European) atmosphere, even the exotic, rustic and romantic Transylvanian feel - SEE the new attachment for inspiration (this was a design plan which we discarded (mainly because of its gothic, (nazi-like), unreadable font, and the fact that the plan makes the black-looking dogs appear brown), however we loved the fact that it was not full of boxes/windows, had a marble/sand stone like continuous background, lots of little elegant graphics, the drawings embedded, etc.
Nice to have
• - Working on smartphone, Zentabs, etc., so dynamic website design
- Web shop to be added to functionalities in the future (?)
- English language for now, in the future can be Hungarian, Romanian, etc., so the font choice should handle various alphabets
- Focus on the dogs (likely more graphics than photos, at least on the main pages), and not on the activities/humans - the design should accentuate the black and not the tan of the graphics!
Should not have
• - Old logo from the old www.brennicksetter.com webpage or the other logo from the Chatterly site of the Brennick Setter Club, we will have a new one (maybe designed by you!)
- Breed club, kennel club cliches
- Cutesy, adorable, cheesy design elements
- Old, stale, monolithic, archaic, snobbish, etc. look and feel
- No vampire associations

```html
<!DOCTYPE html>
<html lang="en">
<head>
<meta charset="utf-8">
<title>Brennick Setter Club</title>
<link href="https://fonts.googleapis.com/css2?family=Oswald:wght@400&family=PT+Sans:wght@400;700&family=PT+Sans+Narrow&display=swap" rel="stylesheet">
<style>
:root{
  --red:#e4322c;
  --gold:#f0a51c;
  --gold-dark:#c8820c;
  --ink:#1b1b1b;
  --text:#444;
  --muted:#666;
  --frame:#e8e5e5;
  --panel:#f1f0ef;
  --tick:#4fb52c;
}
*{box-sizing:border-box;margin:0;padding:0}
html,body{width:802px;height:1200px;overflow:hidden;background:#fff}
body{position:relative;font-family:"PT Sans",sans-serif;color:var(--text)}
.abs{position:absolute}

/* header */
.brand{left:92px;top:4px;display:flex;align-items:center;gap:6px}
.brand-mark{width:60px;height:60px;border-radius:50%;background:var(--gold);border:3px solid var(--ink)}
.brand-name{font-family:"Oswald",sans-serif;font-size:13px;line-height:1.1;color:var(--ink);width:70px}
.account{left:432px;top:9px;font-size:9px;letter-spacing:.3px;color:var(--red)}
.cart{left:551px;top:9px;font-size:9px;color:var(--ink)}
.social{left:604px;top:5px;display:flex;gap:4px}
.social span{width:20px;height:20px;background:#eee;border:1px solid #ddd}
.util{left:493px;top:35px;font-size:9px;color:var(--ink)}
.util b{font-weight:400;margin:0 7px}
.search{left:602px;top:33px;width:94px;height:18px;border:1px solid #555;font-size:9px;padding:3px 6px;color:#222}
.go{left:700px;top:33px;width:20px;height:18px;background:var(--ink);color:#fff;font-size:8px;text-align:center;line-height:18px}
.nav{left:216px;top:64px;width:504px;height:22px;background:var(--gold);border-radius:4px;box-shadow:0 2px 0 var(--gold-dark);display:flex;align-items:center;padding-left:6px}
.nav a{font-size:8px;color:var(--ink);text-decoration:none;padding:0 7px;line-height:22px;white-space:nowrap}
.nav a.active{background:var(--ink);color:#fff;padding:0 6px}

/* hero */
.hero{left:86px;top:105px;width:387px;height:297px;background:var(--panel);padding:4px}
.hero-art{width:100%;height:100%;background:radial-gradient(ellipse at 55% 40%,#6b4a33 0%,#a57a55 30%,#d9cbb8 62%,#ece6dc 100%)}
.hero-caption{left:122px;top:349px;width:316px;height:26px;background:var(--red);color:#fff;font-size:15px;text-align:center;line-height:26px;letter-spacing:.3px}
.hero-sub{left:86px;top:380px;width:387px;text-align:center;font-size:8px;color:#333}
.arrow{top:362px}
.welcome{left:492px;top:105px;width:224px;height:297px;background:var(--panel);padding:10px 13px}
.welcome h2{font-weight:700;font-size:11px;color:var(--red);line-height:1.1}
.welcome h1{font-weight:700;font-size:16px;color:var(--ink);line-height:1.2;letter-spacing:.3px;margin-top:2px}
.welcome p{font-size:7.5px;line-height:1.55;text-align:justify;margin-top:5px;color:#444}
.welcome .more{display:block;text-align:right;font-size:7.5px;color:var(--red);margin-top:3px}
.welcome-art{left:496px;top:258px;width:217px;height:140px;background:radial-gradient(ellipse at 50% 45%,#3b3532 0%,#8b7d6c 40%,#dcd0b6 80%)}

/* sections */
.section{top:430px;height:196px;background:var(--panel);padding:6px}
.section-inner{background:#fff;height:100%;text-align:center;box-shadow:0 4px 4px -3px #aaa}
.section .avatar{width:42px;height:42px;border-radius:50%;border:2px solid var(--gold);margin:4px auto 0;background:radial-gradient(circle at 50% 45%,#4a3a30,#8a6a4f)}
.section h3{font-family:"Oswald",sans-serif;font-weight:400;font-size:17px;color:var(--ink);margin-top:4px;letter-spacing:.2px}
.section ul{list-style:none;font-family:"PT Sans Narrow",sans-serif;font-size:7.5px;line-height:1.45;color:#333;text-align:left;display:inline-block;margin-top:6px;height:70px}
.btn{display:inline-block;background:var(--red);color:#fff;font-family:"PT Sans Narrow",sans-serif;font-size:8px;border-radius:3px;padding:3px 10px;letter-spacing:.3px}
.section .btn{margin-top:2px}

/* listings */
.listing{width:200px}
.photo{height:110px;background:var(--frame);padding:6px}
.photo div{height:100%}
.listing .head{display:flex;justify-content:space-between;margin-top:10px;height:25px}
.listing .kind{font-size:14px;color:var(--ink)}
.listing .price{text-align:right;color:var(--red);font-size:13px;line-height:1}
.listing .price small{display:block;color:#555;font-size:8px;margin-top:1px}
.row{display:flex;font-size:7.5px;color:#444;height:16px;align-items:center}
.row.rule{border-bottom:1px solid #ccc;height:17px;margin-bottom:2px}
.row .l{width:50px}
.row .v{width:46px}
.row .c{width:88px;text-align:right;padding-right:6px;color:#444}
.foot{display:flex;justify-content:flex-end;align-items:center;gap:9px;margin-top:8px;font-size:7.5px;color:var(--red)}
.foot .btn{border-radius:9px;font-family:"PT Sans",sans-serif;font-size:7px;padding:3px 9px}

/* footer */
.footer-line{left:77px;width:650px;height:1px}
.copy{left:90px;top:1162px;font-size:7.5px;color:#333}
.seal{top:1148px;width:34px;height:34px;border-radius:50%;background:#e3e6ea;border:1px solid #b9c0c8}
</style>
</head>
<body>

<header>
  <div class="abs brand"><span class="brand-mark"></span><span class="brand-name">Brennick Setter Club</span></div>
  <div class="abs account">MY ACCOUNT &nbsp;OR&nbsp; LOG &nbsp;IN</div>
  <div class="abs cart">VIEW CART</div>
  <div class="abs social" aria-label="Social links"><span></span><span></span><span></span><span></span><span></span></div>
  <div class="abs util">HOME<b>|</b>CONTACT US</div>
  <div class="abs search">SEARCH HERE..</div>
  <div class="abs go">GO</div>
  <nav class="abs nav">
    <a class="active">ABOUT THE KOPÓ</a><a>LIFE WITH A KOPÓ</a><a>FINDING A KOPÓ</a><a>THE BRENNICK SETTER CLUB</a><a>NEWS AND EVENTS</a><a>SHOP</a>
  </nav>
</header>

<section>
  <div class="abs hero"><div class="hero-art" role="img" aria-label="Drawing of a hound's head"></div></div>
  <div class="abs hero-caption">SMALL BANDNAS FOR YOUR LITTLE BUDDY</div>
  <div class="abs hero-sub">WE HAVE BANDANAS FOR DOGS 20 POUNDS AND UP.</div>
  <svg class="abs arrow" style="left:98px" width="16" height="22" viewBox="0 0 16 22"><path d="M13 2 3 11l10 9" fill="none" stroke="#333" stroke-width="4"/></svg>
  <svg class="abs arrow" style="left:448px" width="16" height="22" viewBox="0 0 16 22"><path d="M3 2l10 9-10 9" fill="none" stroke="#333" stroke-width="4"/></svg>

  <div class="abs welcome">
    <h2>WELCOME TO THE</h2>
    <h1>BRENNICK SETTER CLUB!</h1>
    <p>Transylvanian Hound is one of the most elegant and sophisticated looking ancient Hugarian hunting dog. Their body structure developed and influenced by the special climate &amp; terrain conditions of the Carpathian basin, &amp; which appearance reflects harmony &amp; nobility.</p>
    <a class="more">Read more &gt;&gt;</a>
  </div>
  <div class="abs welcome-art" role="img" aria-label="Drawing of a seated hound"></div>
</section>

<section>
  <div class="abs section" style="left:86px;width:148px"><div class="section-inner">
    <div class="avatar" role="img" aria-label="Hound portrait"></div><h3>ABOUT THE KOPÓ</h3>
    <ul><li>- BREED HISTORY</li><li>- BREED STANDARD</li><li>- PUBLIC EDUCATION</li><li>- PHOTO GALLERY</li></ul><br><span class="btn">READ MORE</span></div></div>
  <div class="abs section" style="left:242px;width:148px"><div class="section-inner">
    <div class="avatar" role="img" aria-label="Puppy portrait"></div><h3>LIFE WITH A KOPÓ</h3>
    <ul><li>- HEALTH AND GENETICS</li><li>- FEEDING AND NUTRITION</li><li>- TRAINING AND ACTIVITIES</li></ul><br><span class="btn">READ MORE</span></div></div>
  <div class="abs section" style="left:398px;width:155px"><div class="section-inner">
    <div class="avatar" role="img" aria-label="Hound portrait"></div><h3>FINDING A KOPÓ</h3>
    <ul><li>- IS THIS THE RIGHT BREED FOR YOU?</li><li>- CHOOSING A PUPPY</li><li>- BREEDER REFERRAL</li><li>- FAQ</li></ul><br><span class="btn">READ MORE</span></div></div>
  <div class="abs section" style="left:561px;width:155px"><div class="section-inner">
    <div class="avatar" role="img" aria-label="Hound portrait"></div><h3>OUR CLUB</h3>
    <ul><li>- CONSTITUTION</li><li>- OFFICERS AND APPOINTEES</li><li>- CODE OF ETHICS</li><li>- BREEDER GUIDELINES</li><li>- MEMBERSHIP</li><li>- REPORTS</li></ul><br><span class="btn">READ MORE</span></div></div>
</section>

<svg width="0" height="0" style="position:absolute"><symbol id="tick" viewBox="0 0 12 10"><path d="M1 5l3.5 3.5L11 1.5" fill="none" stroke="#4fb52c" stroke-width="2.4"/></symbol></svg>

<main>
  <article class="abs listing" style="left:86px;top:656px">
    <div class="photo"><div role="img" aria-label="Puppy chewing a bone" style="background:linear-gradient(#8d8a86,#b8aea8)"></div></div>
    <div class="head"><span class="kind">Puppies</span><span class="price">$1,450 USD<small>[€ 1.068 ]</small></span></div>
    <div class="row rule"><span class="l">Breed:</span>Akita Inu</div>
    <div class="row"><span class="l">Gender:</span><span class="v">Female</span><span class="c">Champion bloodline:</span><svg width="12" height="10"><use href="#tick"/></svg></div>
    <div class="row"><span class="l">Age</span><span class="v">7 month</span><span class="c">Champion sire/Dum:</span><svg width="12" height="10"><use href="#tick"/></svg></div>
    <div class="foot">Remember Marta Delacroix<span class="btn">VIEW DEATILS</span></div>
  </article>
  <article class="abs listing" style="left:300px;top:656px">
    <div class="photo"><div role="img" aria-label="Two newborn puppies in a hand" style="background:linear-gradient(#3a302b,#6e5848)"></div></div>
    <div class="head"><span class="kind">Puppies</span><span class="price">$1,450 USD<small>[€ 1.068 ]</small></span></div>
    <div class="row rule"><span class="l">Breed:</span>Akita Inu</div>
    <div class="row"><span class="l">Gender:</span><span class="v">Female</span><span class="c">Champion bloodline:</span><svg width="12" height="10"><use href="#tick"/></svg></div>
    <div class="row"><span class="l">Age</span><span class="v">7 month</span><span class="c">Champion sire/Dum:</span><svg width="12" height="10"><use href="#tick"/></svg></div>
    <div class="foot">Remember Marta Delacroix<span class="btn">VIEW DEATILS</span></div>
  </article>
  <article class="abs listing" style="left:514px;top:656px">
    <div class="photo"><div role="img" aria-label="Young hound stretching on grass" style="background:linear-gradient(#7f9468,#5f7a4a)"></div></div>
    <div class="head"><span class="kind">Junior</span><span class="price">$1,450 USD<small>[€ 1.068 ]</small></span></div>
    <div class="row rule"><span class="l">Breed:</span>Akita Inu</div>
    <div class="row"><span class="l">Gender:</span><span class="v">Female</span><span class="c">Champion bloodline:</span><svg width="12" height="10"><use href="#tick"/></svg></div>
    <div class="row"><span class="l">Age</span><span class="v">7 month</span><span class="c">Champion sire/Dum:</span><svg width="12" height="10"><use href="#tick"/></svg></div>
    <div class="foot">Remember Marta Delacroix<span class="btn">VIEW DEATILS</span></div>
  </article>

  <article class="abs listing" style="left:86px;top:894px">
    <div class="photo"><div role="img" aria-label="Young hound standing on lawn" style="background:linear-gradient(#9aa58c,#5d7a44)"></div></div>
    <div class="head"><span class="kind">Junior</span><span class="price">$1,450 USD<small>[€ 1.068 ]</small></span></div>
    <div class="row rule"><span class="l">Breed:</span>Akita Inu</div>
    <div class="row"><span class="l">Gender:</span><span class="v">Female</span><span class="c">Champion bloodline:</span><svg width="12" height="10"><use href="#tick"/></svg></div>
    <div class="row"><span class="l">Age</span><span class="v">7 month</span><span class="c">Champion sire/Dum:</span><svg width="12" height="10"><use href="#tick"/></svg></div>
    <div class="foot">Remember Marta Delacroix<span class="btn">VIEW DEATILS</span></div>
  </article>
  <article class="abs listing" style="left:300px;top:894px">
    <div class="photo"><div role="img" aria-label="Close portrait of an adult hound" style="background:linear-gradient(#e4e2e0,#8a7a6c)"></div></div>
    <div class="head"><span class="kind">Adult</span><span class="price">$1,450 USD<small>[€ 1.068 ]</small></span></div>
    <div class="row rule"><span class="l">Breed:</span>Akita Inu</div>
    <div class="row"><span class="l">Gender:</span><span class="v">Female</span><span class="c">Champion bloodline:</span><svg width="12" height="10"><use href="#tick"/></svg></div>
    <div class="row"><span class="l">Age</span><span class="v">7 month</span><span class="c">Champion sire/Dum:</span><svg width="12" height="10"><use href="#tick"/></svg></div>
    <div class="foot">Remember Marta Delacroix<span class="btn">VIEW DEATILS</span></div>
  </article>
  <article class="abs listing" style="left:514px;top:894px">
    <div class="photo"><div role="img" aria-label="Adult hound with red collar outdoors" style="background:linear-gradient(#cfd6c8,#4f6a3a)"></div></div>
    <div class="head"><span class="kind">Adult</span><span class="price">$1,450 USD<small>[€ 1.068 ]</small></span></div>
    <div class="row rule"><span class="l">Breed:</span>Akita Inu</div>
    <div class="row"><span class="l">Gender:</span><span class="v">Female</span><span class="c">Champion bloodline:</span><svg width="12" height="10"><use href="#tick"/></svg></div>
    <div class="row"><span class="l">Age</span><span class="v">7 month</span><span class="c">Champion sire/Dum:</span><svg width="12" height="10"><use href="#tick"/></svg></div>
    <div class="foot">Remember Marta Delacroix<span class="btn">VIEW DEATILS</span></div>
  </article>
</main>

<footer>
  <div class="abs footer-line" style="top:1152px;background:var(--red)"></div>
  <div class="abs copy">Copyright © 2014 Brennick Setter Club</div>
  <div class="abs seal" style="left:631px"></div>
  <div class="abs seal" style="left:672px"></div>
  <div class="abs footer-line" style="top:1178px;background:#333"></div>
</footer>

</body>
</html>
```